Book Cover needs A GREAT Design

I need a book cover designed for my book "Quiet Harbors, Waking to Bloom,
subtitle "Reading the Grammar of Night Visions", by Marion Vaughtley. The book cover needs to reflect the inner contents of the book which is how to understand the symbolic transformational images within our dreams.

Dreams speak to us in a rich visual vocabulary. We dreamed before we had a written language. I want a book cover that uses imagery to draw the reader into the book.

In the language of dreams whenever death occurs it symbolizes a profound pyschological transformation. My clients are all ages 18 to 88+, I want a cover that engages people's unconscious knowing when they look at it. Book Cover formatted to 8.5" x 5.5" I need a high resolution cover, minimum 300dpi so that the cover prints well.

Please save a space for the ISBN Number. The book will be 150-200 pages.
I have attached a photo of myself, for a small picture of me on the back cover. Book will be about 150 pages. Thanks.
Updates

 Author name on the cover: Marion Vaughtley

Reason: I am extending the deadline for 7 days. I have had my own deadline for a project which is tomorrow, so I cannot do anything else unitl that Report is complete. Thank you, Marion

Thank you all for your submissions. I extended the deadline so that I can deal with a report that I have to have done by tomorrow. So book cover has been on the back burner.

Target Market(s)

Any one who wants to gain greater understanding from their dreams. My clients are mostly 18 to 88, I developed the BRIDGE™ Method to help people interpret their dreams, run Dream Groups and Workshops with Art from Dreams. I focus on the holistic, integrative health and wholeness of body mind, and spirit shown in dreams. Especially physical health.

Colors
f04a50
e567a6
a54599
0692cc
ec1f27
3276b5

Requirements
Must have
• I want the cover to be bright vibrant colors peachy pinks, a bit of purplish magenta, and perhaps turquoise blue. I want a transformational image on the front, like a phoenix rising from the ashes. I do not want a stark photographic look. The image must have a dream like quality. I would like the main part of the title font to be a bit shadowed, and I am open to creative suggestions. Document attached has colors I like. I like the idea of shadowed or reflective font because so much of our psyche hides in the "shadows".
Nice to have
• I really want to focus on a transformational image, to emphasize how dreams come with transformational information for our psyche.
Should not have
• No stark, real photographic images for cover. No dark colors. Nothing neon or sci-fi looking. No business like fonts like Times New Roman.

```html
<!DOCTYPE html>
<html lang="en">
<head>
<meta charset="utf-8">
<title>Quiet Harbors, Waking to Bloom — Book Cover</title>
<link rel="stylesheet" href="https://fonts.googleapis.com/css2?family=Cinzel:wght@400;500&family=Libre+Baskerville:ital,wght@0,400;0,700;1,700&display=swap">
<style>
  :root {
    --plum-deep: #5a0a4a;
    --plum: #781463;
    --magenta-glow: #a21e84;
    --ray: rgba(255, 255, 255, 0.04);
    --flame-gold: #ffd22e;
    --flame-orange: #f7921e;
    --flame-coral: #f04a50;
    --flame-red: #ec1f27;
    --flame-pink: #e567a6;
    --title-white: #fbf6f8;
    --subtitle-lilac: #ecd6ea;
    --author-gold: #ffcc1f;
  }
  html, body {
    margin: 0;
    padding: 0;
    overflow: hidden;
    background: var(--plum-deep);
  }
  .cover {
    position: relative;
    width: 776px;
    height: 1200px;
    overflow: hidden;
    background:
      radial-gradient(ellipse 520px 560px at 300px 900px, rgba(162, 30, 132, 0.7), transparent 72%),
      repeating-conic-gradient(from 0deg at 260px 1050px, var(--ray) 0deg 4deg, transparent 4deg 9deg),
      linear-gradient(180deg, var(--plum-deep) 0%, var(--plum) 60%, var(--magenta-glow) 100%);
  }
  .phoenix-art {
    position: absolute;
    left: 0;
    top: 0;
    width: 776px;
    height: 1200px;
  }
  .title-block {
    position: absolute;
    left: 300px;
    width: 450px;
    top: 828px;
    text-align: center;
    color: var(--title-white);
  }
  .title-block h1,
  .title-block p {
    margin: 0;
    font-weight: inherit;
  }
  .title-small {
    display: block;
    font-family: "Cinzel", serif;
    font-weight: 500;
    font-size: 40px;
    letter-spacing: 8px;
    line-height: 44px;
    text-shadow: 2px 3px 4px rgba(40, 0, 30, 0.65);
  }
  .title-large {
    display: block;
    font-family: "Cinzel", serif;
    font-weight: 400;
    font-size: 84px;
    line-height: 88px;
    letter-spacing: 1px;
    text-shadow: 3px 5px 6px rgba(40, 0, 30, 0.7), 0 0 14px rgba(255, 255, 255, 0.15);
  }
  .tagline {
    display: flex;
    align-items: center;
    gap: 12px;
    margin-top: 18px !important;
    font-family: "Cinzel", serif;
    font-size: 25px;
    letter-spacing: 2px;
    color: var(--subtitle-lilac);
  }
  .tagline::before,
  .tagline::after {
    content: "";
    flex: 1;
    height: 1px;
    background: var(--subtitle-lilac);
  }
  .subtitle {
    margin-top: 16px !important;
    font-family: "Libre Baskerville", serif;
    font-weight: 700;
    font-size: 20px;
    line-height: 29px;
    letter-spacing: 1px;
    color: var(--subtitle-lilac);
  }
  .byline {
    margin-top: 16px !important;
    font-family: "Libre Baskerville", serif;
    font-weight: 700;
    font-size: 16px;
    color: var(--subtitle-lilac);
  }
  .author {
    margin-top: 4px !important;
    font-family: "Libre Baskerville", serif;
    font-style: italic;
    font-weight: 700;
    font-size: 23px;
    color: var(--author-gold);
  }
</style>
</head>
<body>
  <main class="cover">
    <svg class="phoenix-art" viewBox="0 0 776 1200" role="img" aria-label="Illustration of a golden and crimson phoenix rising with spread wings, its head to the right and two long flowing tail plumes trailing down to the lower left">
      <defs>
        <linearGradient id="flame-glow" x1="0.7" y1="0" x2="0.3" y2="1">
          <stop offset="0%" stop-color="var(--flame-gold)"/>
          <stop offset="30%" stop-color="var(--flame-orange)"/>
          <stop offset="55%" stop-color="var(--flame-coral)"/>
          <stop offset="80%" stop-color="var(--flame-red)"/>
          <stop offset="100%" stop-color="var(--flame-pink)"/>
        </linearGradient>
        <filter id="soft-edge" x="-20%" y="-20%" width="140%" height="140%">
          <feGaussianBlur stdDeviation="38"/>
        </filter>
      </defs>
      <polygon
        points="0,390 200,310 460,240 600,30 690,330 540,460 380,600 400,800 450,1170 300,1170 70,1070 240,860 260,580 0,480"
        fill="url(#flame-glow)" filter="url(#soft-edge)" opacity="0.85"/>
    </svg>

    <header class="title-block">
      <h1>
        <span class="title-small">QUIET</span>
        <span class="title-large">HARBORS</span>
      </h1>
      <p class="tagline">WAKING TO BLOOM</p>
      <p class="subtitle">Reading the Grammar<br>of Night Visions</p>
      <p class="byline">by</p>
      <p class="author">Marion Vaughtley</p>
    </header>
  </main>
</body>
</html>
```